Commercial photographer, UAV drone photography & 360 walk-through visuals

I need a business card design that is minimalist but yet pretentiously creative. My target market are architects, designers, advertising agents and marketing managers. It is important to stress that though I am asking for a minimalist design it needs to have creative impact.

Target Market(s)

Architects, interiors designers, web-designers, artists

Contact Information for Business Card

Include my name, mobile [cell] number, email, web page and the company logo. Do not to include a postal address.

Colors

Designer to choose colors to be used in the design.

Requirements
Must have
• The following information is to be included:
• Miles Perrow
• Photographer
• m: 07812 593174
• e: miles@mpframeworks.co.uk
• w: mpframeworks.co.uk

```html
<!DOCTYPE html>
<html lang="en">
<head>
<meta charset="utf-8">
<title>MP Frameworks — Business Card</title>
<link rel="stylesheet" href="https://fonts.googleapis.com/css2?family=Montserrat:wght@400;500;700&display=swap">
<style>
  :root {
    --bg: #161616;
    --card: #242424;
    --card-edge: #2e2e2e;
    --ink: #f2f2f2;
    --ink-soft: #c9c9c9;
    --rule: #8a8a8a;
  }
  * { margin: 0; padding: 0; box-sizing: border-box; }
  html, body {
    width: 1200px;
    height: 960px;
    overflow: hidden;
    background: var(--bg);
    font-family: "Montserrat", Arial, sans-serif;
    color: var(--ink);
  }
  .canvas {
    position: relative;
    width: 1200px;
    height: 960px;
  }
  .card {
    position: absolute;
    top: 337px;
    width: 500px;
    height: 286px;
    background: linear-gradient(135deg, var(--card-edge) 0%, var(--card) 55%, #1f1f1f 100%);
    border-radius: 4px;
    box-shadow: 0 18px 40px rgba(0, 0, 0, 0.55);
    display: flex;
    flex-direction: column;
    align-items: center;
    justify-content: center;
  }
  .card--front { left: 70px; }
  .card--back { left: 630px; }

  .brand {
    display: flex;
    align-items: center;
    gap: 10px;
  }
  .brand__dot {
    width: 12px;
    height: 12px;
    border-radius: 50%;
    background: var(--ink);
  }
  .brand__name {
    font-weight: 500;
    font-size: 26px;
    letter-spacing: 0.14em;
    text-transform: uppercase;
    color: var(--ink);
  }
  .card--back .brand__name { font-size: 30px; }

  .contact {
    margin-top: 30px;
    text-align: center;
  }
  .contact__name {
    font-weight: 700;
    font-size: 16px;
    letter-spacing: 0.16em;
    text-transform: uppercase;
  }
  .contact__title {
    margin-top: 2px;
    font-size: 11px;
    color: var(--ink-soft);
  }
  .contact__rule {
    width: 46px;
    height: 1px;
    background: var(--rule);
    margin: 8px auto 8px;
  }
  .contact__line {
    font-size: 11px;
    line-height: 1.45;
    color: var(--ink);
  }
</style>
</head>
<body>
  <main class="canvas">
    <section class="card card--front" aria-label="Card front">
      <div class="brand">
        <span class="brand__dot"></span>
        <span class="brand__name">MP Frameworks</span>
      </div>
      <div class="contact">
        <p class="contact__name">Miles Perrow</p>
        <p class="contact__title">Photographer</p>
        <div class="contact__rule"></div>
        <p class="contact__line">P: 07812 593174</p>
        <p class="contact__line">E: miles@mpframeworks.co.uk &nbsp;|&nbsp; W: mpframeworks.co.uk</p>
      </div>
    </section>

    <section class="card card--back" aria-label="Card back">
      <div class="brand">
        <span class="brand__dot"></span>
        <span class="brand__name">MP Frameworks</span>
      </div>
    </section>
  </main>
</body>
</html>
```